Bref créative
Overseas Capital Partners
I need single sided standard sized Business Card [3.5" x 2"]
May be same as in logo, may be another
Professional
Marek Dobrzyn
Manager
ul. Lipowa 17
41-806 Katowice
Poland
marek.dobrzyn@korvant.com.pl
www.korvant.com.pl

```html
<!DOCTYPE html>
<html lang="en">
<head>
<meta charset="utf-8">
<title>Korvant – Stationery Set</title>
<link rel="stylesheet" href="https://fonts.googleapis.com/css2?family=Raleway:wght@500&family=Open+Sans:wght@400;600&display=swap">
<style>
  :root{
    --board:#1b1c1f;
    --board-light:#2a2b2f;
    --blue:#1f7dc4;
    --blue-deep:#155f9c;
    --sky:#5fc0ec;
    --sky-pale:#a9def6;
    --paper:#ffffff;
    --ink:#3a4550;
    --caption:#7c8188;
  }
  *{margin:0;padding:0;box-sizing:border-box}
  html,body{width:1200px;height:414px;overflow:hidden}
  body{background:radial-gradient(ellipse at 30% 20%,var(--board-light),var(--board) 70%);font-family:"Open Sans",Arial,sans-serif;position:relative}
  .brand{position:absolute;text-align:center}
  .brand-mark{display:block;margin:0 auto;background:var(--sky)}
  .brand-name{font-family:"Raleway",Arial,sans-serif;font-weight:500;letter-spacing:.32em;color:var(--sky);display:block}
  .brand-tag{display:block;color:var(--sky-pale);font-size:7px;letter-spacing:.08em;margin-top:3px}
  .hero{left:205px;top:12px;width:180px}
  .hero .brand-mark{width:56px;height:56px}
  .hero .brand-name{font-size:26px;margin-top:10px;padding-left:.32em}

  .card{position:absolute;width:157px;height:90px;box-shadow:0 3px 8px rgba(0,0,0,.55);overflow:hidden;background:var(--paper)}
  .caption{position:absolute;font-size:5px;color:var(--caption);white-space:nowrap}
  .card-split .info{position:absolute;left:8px;top:10px;width:78px;color:var(--ink);font-size:4.6px;line-height:1.45}
  .card-split .info strong{display:block;color:var(--blue);font-size:6px;font-weight:600}
  .card-split .info em{display:block;font-style:normal;margin-bottom:5px}
  .card-split .panel{position:absolute;right:0;top:0;bottom:0;width:64px;background:linear-gradient(160deg,var(--sky),var(--blue))}
  .card-split.alt .panel{background:linear-gradient(160deg,var(--sky-pale),var(--sky))}
  .panel .brand{left:0;right:0;top:24px}
  .mini .brand-mark{width:20px;height:20px;background:var(--paper)}
  .mini .brand-name{font-size:8px;margin-top:5px;color:var(--paper);padding-left:.32em}
  .front .brand{left:0;right:0;top:22px}
  .front.white .brand-mark{background:var(--sky)}
  .front.white .brand-name{color:var(--blue)}
  .front.blue{background:linear-gradient(160deg,var(--sky),var(--blue-deep))}
  .front.pale{background:linear-gradient(160deg,var(--sky-pale),var(--sky))}
  .front .brand-name{font-size:11px}
  .front .brand-mark{width:24px;height:24px}

  .letterhead{position:absolute;left:538px;top:24px;width:211px;height:360px;background:var(--paper);box-shadow:0 4px 12px rgba(0,0,0,.6)}
  .letterhead .head{position:absolute;left:14px;top:12px}
  .letterhead .brand{position:static;text-align:left}
  .letterhead .brand-mark{width:16px;height:16px;margin:0}
  .letterhead .brand-name{font-size:6px;color:var(--blue);margin-top:3px;letter-spacing:.2em}
  .letterhead .address{position:absolute;right:14px;top:12px;font-size:4.2px;line-height:1.5;color:var(--ink)}
  .letterhead .watermark{position:absolute;left:60px;top:110px;width:90px;height:90px;border-radius:50%;background:#eef4f8}
  .letterhead .foot{position:absolute;left:0;right:0;bottom:0;height:6px;background:linear-gradient(90deg,var(--sky),var(--blue))}
  .envelopes{position:absolute;left:812px;top:100px}
</style>
</head>
<body>

  <div class="brand hero">
    <span class="brand-mark"></span>
    <span class="brand-name">KORVANT</span>
    <span class="brand-tag">Overseas Capital Partners</span>
  </div>

  <div class="card card-split" style="left:125px;top:149px">
    <div class="info">
      <strong>Marek Dobrzyn</strong>
      <em>Manager</em>
      ul. Lipowa 17<br>41-806 Katowice, Poland<br>tel. +48 32 555 01 17<br>marek.dobrzyn@korvant.com.pl<br>www.korvant.com.pl
    </div>
    <div class="panel"><div class="brand mini"><span class="brand-mark"></span><span class="brand-name">KORVANT</span></div></div>
  </div>
  <span class="caption" style="left:180px;top:244px">back side</span>

  <div class="card card-split alt" style="left:293px;top:149px">
    <div class="info">
      <strong>Marek Dobrzyn</strong>
      <em>Manager</em>
      ul. Lipowa 17<br>41-806 Katowice, Poland<br>tel. +48 32 555 01 17<br>marek.dobrzyn@korvant.com.pl<br>www.korvant.com.pl
    </div>
    <div class="panel"><div class="brand mini"><span class="brand-mark"></span><span class="brand-name">KORVANT</span></div></div>
  </div>
  <span class="caption" style="left:346px;top:244px">back side</span>

  <div class="card front white" style="left:34px;top:283px">
    <div class="brand"><span class="brand-mark"></span><span class="brand-name">KORVANT</span></div>
  </div>
  <span class="caption" style="left:92px;top:378px">front side</span>

  <div class="card front blue" style="left:202px;top:283px">
    <div class="brand mini"><span class="brand-mark"></span><span class="brand-name">KORVANT</span></div>
  </div>
  <span class="caption" style="left:260px;top:378px">front side</span>

  <div class="card front pale" style="left:367px;top:283px">
    <div class="brand mini"><span class="brand-mark"></span><span class="brand-name">KORVANT</span></div>
  </div>
  <span class="caption" style="left:425px;top:378px">front side</span>

  <div class="letterhead">
    <div class="head">
      <div class="brand"><span class="brand-mark"></span><span class="brand-name">KORVANT</span></div>
    </div>
    <div class="address">ul. Lipowa 17<br>41-806 Katowice<br>Poland<br>tel. +48 32 555 01 17<br>www.korvant.com.pl</div>
    <div class="watermark"></div>
    <div class="foot"></div>
  </div>
  <span class="caption" style="left:628px;top:390px">Letterhead</span>

  <svg class="envelopes" width="360" height="280" viewBox="0 0 360 280" aria-label="Envelopes">
    <defs>
      <linearGradient id="flap" x1="0" y1="0" x2="0" y2="1">
        <stop offset="0" stop-color="#5fc0ec"/><stop offset="1" stop-color="#1f7dc4"/>
      </linearGradient>
    </defs>
    <g transform="rotate(-8 180 60)">
      <rect x="40" y="10" width="300" height="140" fill="#fff"/>
      <path d="M40 10 L190 85 L340 10 Z" fill="url(#flap)"/>
    </g>
    <g transform="rotate(-3 180 100)">
      <rect x="20" y="60" width="320" height="140" fill="#fff"/>
      <path d="M20 60 L180 140 L340 60 Z" fill="url(#flap)"/>
    </g>
    <rect x="0" y="128" width="352" height="138" fill="#fff"/>
    <rect x="0" y="252" width="352" height="14" fill="url(#flap)"/>
    <circle cx="176" cy="196" r="38" fill="#eef4f8"/>
    <rect x="14" y="142" width="14" height="14" fill="#5fc0ec"/>
    <text x="14" y="166" font-family="Raleway, Arial, sans-serif" font-weight="500" font-size="6" letter-spacing="1.2" fill="#1f7dc4">KORVANT</text>
    <text x="168" y="278" font-family="Open Sans, Arial, sans-serif" font-size="5" fill="#7c8188">Envelope</text>
  </svg>

</body>
</html>
```